Eulogy for my Sister Ruth Celestine Wanjiku

I need a beautiful design for my sisters funeral Eulogy/ booklet to use at the funeral . I have the materials but need a designer to make it beautiful

Requirements
Must have
• Pictures and words
Nice to have
• convey love and emotions

```html
<!DOCTYPE html>
<html lang="en">
<head>
<meta charset="utf-8">
<title>In Loving Memory – Ruth Celestine</title>
<link href="https://fonts.googleapis.com/css2?family=Great+Vibes&family=Montserrat:wght@400;500&display=swap" rel="stylesheet">
<style>
  :root {
    --page: #f7f6f6;
    --paper: #f3eced;
    --paper-shade: #ebe3e4;
    --rose: #d9738a;
    --ink: #161414;
    --gold: #c29a62;
    --lavender: #b9b3e6;
    --teal: #7fc1cc;
    --peach: #f5c3a6;
    --sage: #9fb59a;
    --charcoal: #5c5a5b;
  }
  * { margin: 0; padding: 0; box-sizing: border-box; }
  html, body { width: 1200px; height: 608px; overflow: hidden; background: var(--page); }
  .canvas { position: relative; width: 1200px; height: 608px; }

  .card {
    position: absolute; top: 45px; width: 358px; height: 506px;
    background: radial-gradient(ellipse at 30% 40%, var(--paper-shade), transparent 60%),
                radial-gradient(ellipse at 80% 80%, var(--paper-shade), transparent 55%),
                var(--paper);
    font-family: "Montserrat", sans-serif;
    color: var(--ink);
    text-align: center;
  }
  .card--gold { left: 37px; }
  .card--swirl { left: 419px; }
  .card--ink { left: 805px; }

  .frame { position: absolute; inset: 0; width: 100%; height: 100%; }

  .eyebrow {
    position: absolute; top: 80px; left: 0; right: 0;
    font-size: 14px; font-weight: 400; letter-spacing: 0.5px; color: var(--rose);
  }
  .title {
    position: absolute; top: 86px; left: 0; right: 0;
    font-family: "Great Vibes", cursive; font-size: 60px; line-height: 1; font-weight: 400;
  }

  .wreath {
    position: absolute; left: 109px; top: 157px; width: 140px; height: 140px; border-radius: 50%;
  }
  .card--gold .wreath { background: radial-gradient(circle, transparent 52%, var(--lavender) 56%, var(--teal) 68%, transparent 72%); }
  .card--swirl .wreath { background: radial-gradient(circle, transparent 52%, var(--peach) 56%, var(--sage) 68%, transparent 72%); }
  .card--ink .wreath { left: 99px; top: 155px; width: 160px; height: 150px; background: radial-gradient(circle, transparent 46%, #bdbabb 52%, var(--charcoal) 64%, transparent 70%); }

  .portrait {
    position: absolute; left: 125px; top: 173px; width: 108px; height: 108px; border-radius: 50%;
    background: linear-gradient(160deg, #e6e6e6, #8c8c8c);
  }
  .card--gold .portrait, .card--swirl .portrait { border: 1.5px solid var(--gold); }
  .card--ink .portrait { left: 137px; top: 186px; width: 88px; height: 88px; }

  .name {
    position: absolute; top: 318px; left: 0; right: 0;
    font-size: 24px; font-weight: 400; color: var(--rose);
  }
  .card--swirl .name { top: 306px; font-family: "Great Vibes", cursive; font-size: 40px; }

  .dates { position: absolute; top: 351px; left: 0; right: 0; font-size: 10.5px; }
  .card--swirl .dates { top: 356px; }

  .service { position: absolute; top: 398px; left: 0; right: 0; font-size: 7px; line-height: 8px; }

  .ornament { position: absolute; }
  .ornament--top { left: 160px; top: 22px; width: 165px; height: 28px; background: linear-gradient(90deg, transparent, rgba(194,154,98,.35), transparent); border-radius: 14px; }
  .ornament--right { left: 300px; top: 40px; width: 28px; height: 170px; background: linear-gradient(180deg, transparent, rgba(194,154,98,.35), transparent); border-radius: 14px; }
  .ornament--left { left: 20px; top: 296px; width: 30px; height: 170px; background: linear-gradient(180deg, transparent, rgba(194,154,98,.35), transparent); border-radius: 14px; }
  .ornament--bottom { left: 40px; top: 456px; width: 150px; height: 26px; background: linear-gradient(90deg, transparent, rgba(194,154,98,.35), transparent); border-radius: 13px; }
</style>
</head>
<body>
<main class="canvas">

  <article class="card card--gold">
    <svg class="frame" viewBox="0 0 358 506" aria-hidden="true">
      <path d="M61 40 H296 A22 22 0 0 0 318 62 V444 A22 22 0 0 0 296 466 H61 A22 22 0 0 0 39 444 V62 A22 22 0 0 0 61 40 Z" fill="none" stroke="var(--gold)" stroke-width="1"/>
      <rect x="48" y="48" width="261" height="410" fill="none" stroke="var(--gold)" stroke-width="1"/>
    </svg>
    <p class="eyebrow">IN LOVING</p>
    <h1 class="title">memory</h1>
    <div class="wreath" role="img" aria-label="Watercolour wreath of lavender and blue flowers"></div>
    <div class="portrait" role="img" aria-label="Black and white portrait of Ruth"></div>
    <h2 class="name">Ruth Celestine</h2>
    <p class="dates">20th June 1990 - 8th Feb. 2022</p>
    <p class="service">Sunday, Feb 8, 2022, 10:00 AM<br>Name of Church<br>234, Street, City, State</p>
  </article>

  <article class="card card--swirl">
    <svg class="frame" viewBox="0 0 358 506" aria-hidden="true">
      <rect x="39" y="44" width="277" height="421" fill="none" stroke="var(--gold)" stroke-width="0.8"/>
    </svg>
    <div class="ornament ornament--top" role="img" aria-label="Gold swirl flourish"></div>
    <div class="ornament ornament--right" role="img" aria-label="Gold swirl flourish"></div>
    <div class="ornament ornament--left" role="img" aria-label="Gold swirl flourish"></div>
    <div class="ornament ornament--bottom" role="img" aria-label="Gold swirl flourish"></div>
    <p class="eyebrow">IN LOVING</p>
    <h1 class="title">memory</h1>
    <div class="wreath" role="img" aria-label="Watercolour peach roses with green leaves"></div>
    <div class="portrait" role="img" aria-label="Black and white portrait of Ruth"></div>
    <h2 class="name">Ruth Celestine</h2>
    <p class="dates">20th June 1990 - 8th Feb. 2022</p>
    <p class="service">Sunday, Feb 8, 2022, 10:00 AM<br>Name of Church<br>234, Street, City, State</p>
  </article>

  <article class="card card--ink">
    <svg class="frame" viewBox="0 0 358 506" aria-hidden="true">
      <path d="M61 40 H296 A22 22 0 0 0 318 62 V444 A22 22 0 0 0 296 466 H61 A22 22 0 0 0 39 444 V62 A22 22 0 0 0 61 40 Z" fill="none" stroke="var(--ink)" stroke-width="1"/>
      <rect x="48" y="48" width="261" height="410" fill="none" stroke="var(--ink)" stroke-width="1"/>
    </svg>
    <p class="eyebrow">IN LOVING</p>
    <h1 class="title">memory</h1>
    <div class="wreath" role="img" aria-label="Grey hand-drawn leaf wreath"></div>
    <div class="portrait" role="img" aria-label="Black and white portrait of Ruth"></div>
    <h2 class="name">Ruth Celestine</h2>
    <p class="dates">20th June 1990 - 8th Feb. 2022</p>
    <p class="service">Sunday, Feb 8, 2022, 10:00 AM<br>Name of Church<br>234, Street, City, State</p>
  </article>

</main>
</body>
</html>
```